Very High End Grooming Salon needs new business card design

I need a very nice card design I am a certified Master groomer we have a very high end clients. Our color is pink but does not have to be pink. I have a logo also a mission statement .
Fern N Fluff Pet Boutique and Spa
48710 Orchard Rd
Coral Haven FL 34990
555 904 3826
www.fernfluffboutique-example.com
online booking available
this is our mission statement not sure it need to go on card but here it is.
Our Mission is to show respect to all animals pampering them with the same high end tailored service one would expect to receive at a day spa
as the only certified master groomer in the area we strive to put your pets best paw forward.

Industry/Entity Type

Business

```html
<!DOCTYPE html>
<html lang="en">
<head>
<meta charset="utf-8">
<title>Fern N Fluff Pet Boutique and Spa – Business Card</title>
<link href="https://fonts.googleapis.com/css2?family=Cormorant+Garamond:wght@600&display=swap" rel="stylesheet">
<style>
  :root {
    --magenta: #d1156f;
    --blush: #f8a9cb;
    --blush-soft: #fbc3da;
    --white: #ffffff;
    --backdrop: #e9e7e6;
    --card-shadow: rgba(60, 40, 50, 0.22);
  }
  * { box-sizing: border-box; margin: 0; padding: 0; }
  html, body { width: 1200px; height: 900px; overflow: hidden; }
  body {
    background: var(--backdrop);
    font-family: "Cormorant Garamond", "Times New Roman", serif;
    font-weight: 600;
    color: var(--magenta);
    position: relative;
  }
  .card {
    position: absolute;
    width: 620px;
    height: 354px;
    border-radius: 4px;
    overflow: hidden;
    box-shadow: 0 10px 24px var(--card-shadow);
  }
  .card--front { left: 390px; top: 70px; background: var(--magenta); }
  .card--back {
    left: 190px; top: 470px;
    background: repeating-linear-gradient(90deg,
      var(--magenta) 0 26px, var(--blush) 26px 52px);
  }
  .bath-art {
    position: absolute;
    background: var(--white);
    border-radius: 46px 46px 120px 120px;
  }
  .card--front .bath-art { left: 110px; top: 42px; width: 370px; height: 270px; }
  .card--back .bath-art { left: 130px; top: 40px; width: 400px; height: 282px; }
  .booking-band {
    position: absolute;
    right: 0; top: 88px;
    width: 250px; height: 24px;
    background: var(--blush-soft);
    border-radius: 12px 0 0 12px;
    font-size: 14px;
    letter-spacing: 0.06em;
    text-transform: uppercase;
    line-height: 24px;
    padding-left: 16px;
    white-space: nowrap;
  }
  .brand-name {
    position: absolute;
    display: flex;
    align-items: center;
    gap: 10px;
    white-space: nowrap;
  }
  .brand-name .dot {
    width: 14px; height: 14px; border-radius: 50%;
    background: var(--magenta);
  }
  .card--front .brand-name { left: 160px; top: 150px; font-size: 30px; }
  .brand-tagline {
    position: absolute;
    left: 168px; top: 190px;
    font-size: 17px;
    letter-spacing: 0.05em;
    text-transform: uppercase;
    white-space: nowrap;
  }
  .card--back .brand-name { left: 278px; top: 90px; font-size: 21px; }
  .contact {
    position: absolute;
    left: 100px; top: 128px;
    width: 460px;
    text-align: center;
    text-transform: uppercase;
    line-height: 1.15;
    font-style: normal;
    white-space: nowrap;
  }
  .contact__name { font-size: 18px; margin-bottom: 10px; }
  .contact__line { font-size: 17px; }
  .contact__web { font-size: 22px; text-transform: none; margin-top: 6px; }
</style>
</head>
<body>
  <section class="card card--front">
    <div class="bath-art" role="img" aria-label="White silhouette of a dog sitting in a clawfoot bathtub"></div>
    <div class="booking-band">Online Booking Available</div>
    <div class="brand-name"><span>Fern N Fluff</span><span class="dot"></span></div>
    <div class="brand-tagline">Pet Boutique and Spa</div>
  </section>

  <section class="card card--back">
    <div class="bath-art" role="img" aria-label="White silhouette of a dog sitting in a clawfoot bathtub"></div>
    <div class="brand-name"><span>Fern N Fluff</span><span class="dot"></span></div>
    <address class="contact">
      <p class="contact__name">Fern N Fluff Pet Boutique and Spa</p>
      <p class="contact__line">48710 Orchard Rd</p>
      <p class="contact__line">Coral Haven FL 34990</p>
      <p class="contact__line">555 904 3826</p>
      <p class="contact__web">www.fernfluffboutique-example.com</p>
    </address>
  </section>
</body>
</html>
```